Quarvelon stickers design for our main topics (for example: agile and Kanban)

We are looking for sticker design, that will reflect our cooperate identity and can be used for the different topics in our company. We would like to start with our Agile Coaching Offers with a Kanban Sticker saying "stop starting, start finishing", A bad example can be find in the file upload ;)
Check out our homepage to get a feeling for the cooperate identity (www.quarvelon-beispiel.ch)

Target Market(s)

Customers and trainees from our trainings

Industry/Entity Type

Consulting

Colors
0355a3
fbed22

Requirements
Must have
• a cool design thats fits to our customer design
the 2 lines can be changed for future stickers ... like in the example "stop starting, start finishing" and "we show you how"
Nice to have
• -
Should not have
• -

```html
<!DOCTYPE html>
<html lang="en">
<head>
<meta charset="utf-8">
<title>Quarvelon Sticker – Stop Starting, Start Finishing</title>
<link rel="stylesheet" href="https://fonts.googleapis.com/css2?family=Poppins:wght@400;800&display=swap">
<style>
  :root {
    --backdrop-top: #98b7fb;
    --backdrop-bottom: #8aa9ea;
    --brand-blue: #0a3ff0;
    --brand-yellow: #fbfaa6;
    --sticker-white: #ffffff;
    --ink-dark: #1b1b1f;
  }
  * { margin: 0; padding: 0; box-sizing: border-box; }
  html, body { width: 1200px; height: 1200px; overflow: hidden; }
  body {
    background: linear-gradient(180deg, var(--backdrop-top), var(--backdrop-bottom));
    font-family: "Poppins", sans-serif;
  }
  .canvas { position: relative; width: 1200px; height: 1200px; }
  .sticker-shape { position: absolute; inset: 0; filter: drop-shadow(0 6px 10px rgba(30, 50, 110, 0.25)); }
  .headline {
    position: absolute;
    left: 532px;
    width: 560px;
    top: 532px;
    text-align: center;
    color: var(--brand-blue);
    font-weight: 800;
    font-size: 57px;
    line-height: 70px;
    letter-spacing: -1.5px;
  }
  .footer-row {
    position: absolute;
    left: 504px;
    width: 572px;
    top: 700px;
    height: 56px;
    display: flex;
    align-items: center;
    justify-content: space-between;
  }
  .tagline {
    color: var(--brand-blue);
    font-weight: 400;
    font-size: 30px;
    line-height: 1;
    letter-spacing: -0.3px;
    white-space: nowrap;
  }
  .company-mark {
    display: flex;
    align-items: center;
    gap: 12px;
  }
  .company-mark__square {
    width: 40px;
    height: 40px;
    background: var(--brand-blue);
    flex: none;
  }
  .company-mark__name {
    color: var(--ink-dark);
    font-weight: 400;
    font-size: 27px;
    line-height: 1;
    white-space: nowrap;
  }
</style>
</head>
<body>
  <main class="canvas">
    <svg class="sticker-shape" width="1200" height="1200" viewBox="0 0 1200 1200">
      <circle cx="332" cy="598" r="232" fill="var(--sticker-white)"/>
      <rect x="424" y="500" width="704" height="304" rx="72" fill="var(--sticker-white)"/>
      <rect x="436" y="512" width="680" height="280" rx="62" fill="var(--brand-yellow)"/>
      <rect x="448" y="524" width="656" height="256" rx="50" fill="var(--sticker-white)"/>
      <circle cx="332" cy="598" r="198" fill="var(--brand-yellow)"/>
      <circle cx="332" cy="598" r="188" fill="var(--brand-blue)" role="img"
        aria-label="Illustration of a white rocket with a yellow trail orbiting a blue planet with yellow stars"/>
    </svg>

    <h1 class="headline">STOP STARTING,<br>START FINISHING!</h1>

    <div class="footer-row">
      <p class="tagline">We show you how ...</p>
      <div class="company-mark">
        <span class="company-mark__square"></span>
        <span class="company-mark__name">quarvelon ag</span>
      </div>
    </div>
  </main>
</body>
</html>
```